tri-fold brochure design for psychology practice - all content provided

we are a psychology practice that specialises in diagnostic and educational assessments for children, adolescents and adults. We have an existing logo and I am attaching a word doc (tri-fold brochure) with the required content. I am also attaching our logo and other relevant content docs. The layout is only a sample and we are looking for someone to put this together into a consistent and better layout.

Target Market(s)

parents

Industry/Entity Type

education and health

Font styles to use
Other font styles liked:
• crimsonpro

Requirements
Must have
• our logo and the provided content

```html
<!DOCTYPE html>
<html lang="en">
<head>
<meta charset="utf-8">
<title>brightpath – tri-fold brochure</title>
<link href="https://fonts.googleapis.com/css2?family=Crimson+Pro:wght@400;500&family=Montserrat:wght@500;600;700&family=Open+Sans:wght@400;600;700&display=swap" rel="stylesheet">
<style>
:root{
  --stage:#5b5b5b;
  --paper:#ffffff;
  --paper-soft:#f1f2f0;
  --green-deep:#4d8a36;
  --green:#5cb96b;
  --green-text:#4f9a3c;
  --blue:#4a8fd6;
  --ink:#3a3a3a;
  --ink-soft:#555;
  --label:#e6e6e6;
}
*{box-sizing:border-box;margin:0;padding:0}
html,body{width:1200px;height:4183px;overflow:hidden}
body{background:var(--stage);font-family:"Open Sans",Arial,sans-serif;color:var(--ink);position:relative}
.sheet-label{position:absolute;left:130px;font-family:"Montserrat",Arial,sans-serif;font-weight:500;font-size:17px;letter-spacing:3px;color:var(--label)}
.spread{position:absolute;left:91px;width:1018px;height:715px;display:flex;box-shadow:0 6px 18px rgba(0,0,0,.35)}
.panel{width:339.33px;height:100%;position:relative;text-align:center;overflow:hidden}
.panel-white{background:var(--paper)}
.panel-soft{background:var(--paper-soft)}
.wordmark{font-family:"Crimson Pro",Georgia,serif;font-weight:500;color:var(--ink);display:flex;align-items:center;justify-content:center;gap:8px}
.wordmark .dot{width:14px;height:14px;border-radius:50%;background:var(--green-deep)}
.tagline{font-family:"Crimson Pro",Georgia,serif;font-size:12px;color:var(--ink-soft);margin-top:2px}
.web{font-size:12px;color:var(--ink)}
.web b{font-weight:700}
/* outside: steps */
.step-icon{position:absolute;left:50%;transform:translateX(-50%);width:62px;height:62px;border-radius:50%;display:flex;align-items:center;justify-content:center}
.step-box{position:absolute;left:42px;width:255px;border:2px solid;border-radius:4px;padding:30px 14px 12px;font-size:11.5px;line-height:1.45}
.step-box h3{font-family:"Montserrat",Arial,sans-serif;font-weight:600;font-size:15px;margin-bottom:8px}
.blue{--c:var(--blue)}
.green{--c:var(--green)}
.step-box{border-color:var(--c)}
.step-box h3{color:var(--c)}
.step-icon{background:var(--c)}
.connector{position:absolute;left:50%;width:2px;background:var(--c);transform:translateX(-50%)}
.connector::after{content:"";position:absolute;left:-5px;bottom:-6px;border:6px solid transparent;border-top-color:var(--c);border-bottom:0}
/* contact */
.branch{position:absolute;left:0;top:260px;width:339px;height:175px;background:linear-gradient(160deg,#e7ebe3,#d6dfcf)}
.touch{position:absolute;top:465px;width:100%;font-family:"Montserrat",Arial,sans-serif;font-size:18px;line-height:1.2}
.touch strong{color:var(--green-text);font-weight:600;display:block}
.touch span{font-weight:500;color:var(--ink)}
.contact-icons{position:absolute;top:543px;width:100%;display:flex;justify-content:center;gap:16px}
.contact-icons i{width:26px;height:26px;border-radius:50%;background:var(--green-text);display:flex;align-items:center;justify-content:center}
.contact-lines{position:absolute;top:585px;width:100%;font-size:15.5px;line-height:1.4}
/* cover */
.cover-photo{position:absolute;top:185px;left:0;width:100%;height:332px;background:linear-gradient(135deg,#d9c6b3,#c7b5a5 45%,#e8ddd2)}
.cover-band{position:absolute;top:517px;left:0;width:100%;height:198px;background:var(--green-deep);color:#fff}
.cover-band h1{font-family:"Montserrat",Arial,sans-serif;font-weight:700;font-size:29px;line-height:1.12;letter-spacing:.5px;margin-top:34px}
.cover-band .web{color:#fff;position:absolute;bottom:22px;width:100%}
/* inside */
.inside-photo{position:absolute;top:107px;left:0;width:100%;height:309px;background:linear-gradient(150deg,#eceff0,#d7c9be 55%,#cdb6a6)}
.tag{display:inline-block;font-family:"Montserrat",Arial,sans-serif;font-weight:600;color:#fff;padding:5px 14px;border-radius:4px;font-size:17px;letter-spacing:.5px}
.tag-green{background:var(--green)}
.tag-blue{background:var(--blue)}
.body-copy{font-size:12.2px;line-height:1.42;color:var(--ink-soft)}
.body-copy p+p{margin-top:14px}
.footer-bar{position:absolute;bottom:0;left:0;width:100%;height:55px;display:flex;align-items:center;justify-content:center;font-size:12.5px}
.footer-green{background:var(--green);color:#fff}
.footer-soft{background:#dfe2dd;color:var(--ink)}
.conditions{list-style:none;text-align:left;margin:28px 0 0 60px;font-family:"Montserrat",Arial,sans-serif;font-weight:600;font-size:13.5px;color:var(--ink)}
.conditions li{position:relative;padding:3px 0 3px 28px}
.conditions li::before{content:"";position:absolute;left:0;top:8px;border:6px solid transparent;border-left:9px solid #8a8a8a;border-right:0}
.process{position:absolute;top:48px;left:0;width:100%}
.proc-step{position:absolute;left:0;width:100%;height:98px}
.proc-num{position:absolute;left:30px;top:18px;width:60px;height:60px;border-radius:50%;background:var(--green);border:4px solid #fff;box-shadow:0 0 0 2px var(--green);color:#fff;font-family:"Montserrat",Arial,sans-serif;font-weight:600;font-size:30px;display:flex;align-items:center;justify-content:center}
.proc-box{position:absolute;left:60px;right:36px;top:0;height:96px;border:2px dashed #9fd6a8;border-radius:6px;padding:16px 8px 8px 44px;text-align:left;font-size:11.3px;line-height:1.35;color:var(--ink-soft)}
</style>
</head>
<body>

<div class="sheet-label" style="top:2557px">BROCHURE_OUTSIDE</div>

<section class="spread" style="top:2598px" aria-label="Brochure outside">
  <!-- steps panel -->
  <div class="panel panel-white">
    <div class="blue">
      <div class="step-icon" style="top:20px">
        <svg width="34" height="30" viewBox="0 0 34 30" fill="none" stroke="#fff" stroke-width="2"><circle cx="10" cy="9" r="4"/><circle cx="24" cy="9" r="4"/><path d="M3 26c0-6 3-9 7-9s7 3 7 9M17 26c0-6 3-9 7-9s7 3 7 9"/></svg>
      </div>
      <div class="step-box" style="top:62px;height:150px">
        <h3>UNDERSTANDING</h3>
        Assessment starts with listening first, and then asking the right questions in order to ensure that we are understanding your concerns and hearing your questions.
      </div>
      <div class="connector" style="top:212px;height:30px"></div>
    </div>
    <div class="green">
      <div class="step-icon" style="top:246px">
        <svg width="30" height="30" viewBox="0 0 30 30" fill="none" stroke="#fff" stroke-width="2.5"><circle cx="12" cy="12" r="8"/><path d="M18 18l9 9"/></svg>
      </div>
      <div class="step-box" style="top:279px;height:152px">
        <h3>IDENTIFYING</h3>
        It is then our job to use our diagnostic and assessment knowledge and skills to collect the right data in order to address your concerns and provide answers to your questions.
      </div>
      <div class="connector" style="top:431px;height:30px"></div>
      <div class="step-icon" style="top:466px">
        <svg width="28" height="32" viewBox="0 0 28 32" fill="none" stroke="#fff" stroke-width="2"><path d="M14 2v28M14 6h10l3 4-3 4H14M14 16H5l-3 4 3 4h9"/></svg>
      </div>
      <div class="step-box" style="top:497px;height:153px">
        <h3>GUIDING</h3>
        This then enables us to provide you with recommendations for accessing support and interventions that are based on current best practice and are supported by evidence.
      </div>
    </div>
    <div class="web" style="position:absolute;top:678px;width:100%">www.<b>brightpathclinic</b>.com.au</div>
  </div>

  <!-- contact panel -->
  <div class="panel panel-soft">
    <div style="position:absolute;top:58px;width:100%">
      <div class="wordmark" style="font-size:34px"><span class="dot"></span>brightpath</div>
      <div class="tagline">diagnostic and educational assessments</div>
    </div>
    <div class="branch" role="img" aria-label="Illustration of a leafy tree branch"></div>
    <div class="touch"><strong>GET IN TOUCH</strong><span>WITH US</span></div>
    <div class="contact-icons">
      <i><svg width="12" height="14" viewBox="0 0 12 14"><path d="M6 0a5 5 0 0 0-5 5c0 4 5 9 5 9s5-5 5-9a5 5 0 0 0-5-5z" fill="#fff"/><circle cx="6" cy="5" r="2" fill="#4f9a3c"/></svg></i>
      <i><svg width="14" height="14" viewBox="0 0 14 14"><path d="M3 1l2 3-1.5 1.5a8 8 0 0 0 5 5L10 9l3 2-1 2.5C6 14 0 8 .5 2z" fill="#fff"/></svg></i>
      <i><svg width="14" height="10" viewBox="0 0 14 10" fill="none" stroke="#fff" stroke-width="1.4"><rect x=".7" y=".7" width="12.6" height="8.6" fill="#fff"/><path d="M1 1l6 5 6-5" stroke="#4f9a3c"/></svg></i>
      <i><svg width="14" height="14" viewBox="0 0 14 14" fill="none" stroke="#fff" stroke-width="1.2"><circle cx="7" cy="7" r="6"/><ellipse cx="7" cy="7" rx="2.6" ry="6"/><path d="M1 7h12"/></svg></i>
    </div>
    <div class="contact-lines">
      12/48 Harbour View Rd,<br>Seabrook NSW 2199<br>02 9000 4127<br>hello@brightpathclinic.com.au<br>www.brightpathclinic.com.au
    </div>
  </div>

  <!-- cover panel -->
  <div class="panel panel-white">
    <div style="position:absolute;top:48px;width:100%">
      <div class="wordmark" style="font-size:40px"><span class="dot"></span>brightpath</div>
      <div class="tagline">diagnostic and educational assessments</div>
    </div>
    <div class="cover-photo" role="img" aria-label="Photo of a mother helping her young child draw with coloured pencils"></div>
    <div class="cover-band">
      <h1>UNDERSTANDING<br>IDENTIFYING<br>GUIDING</h1>
      <div class="web">www.<b>brightpathclinic</b>.com.au</div>
    </div>
  </div>
</section>

<div class="sheet-label" style="top:3357px">BROCHURE_INSIDE</div>

<section class="spread" style="top:3400px" aria-label="Brochure inside">
  <!-- who we are -->
  <div class="panel panel-white">
    <div style="position:absolute;top:30px;width:100%">
      <div class="wordmark" style="font-size:32px"><span class="dot"></span>brightpath</div>
      <div class="tagline">diagnostic and educational assessments</div>
    </div>
    <div class="inside-photo" role="img" aria-label="Photo of a teacher reading with a young boy"></div>
    <div style="position:absolute;top:432px;width:100%"><span class="tag tag-green">WHO WE ARE</span></div>
    <div class="body-copy" style="position:absolute;top:480px;left:32px;right:32px">
      <p>The bright path is a team with a passion for helping people to thrive. We are a team of psychologists and teachers who have experience in both educational and clinical settings.</p>
      <p>We understand the challenges parents face in wanting what is best for their children, trying to understand how and where to access the most relevant information and support.</p>
    </div>
    <div class="footer-bar footer-green">Call : 02 9000 4127</div>
  </div>

  <!-- about -->
  <div class="panel panel-soft">
    <div class="body-copy" style="position:absolute;top:38px;left:32px;right:32px">
      <p>We are passionate about wanting to help families navigate the diagnostic and assessment process.</p>
      <p>We believe that quality and comprehensive assessment needs to happen before intervention begins. We work collaboratively with other professionals to ensure that recommendations and supports put in place are appropriate and evidence-based while also meeting the needs of the individual.</p>
      <p>We are qualified to give formal diagnoses for mental health conditions and specific learning disorders. This includes:</p>
    </div>
    <ul class="conditions" style="position:absolute;top:282px;left:0;margin-left:60px">
      <li>Attention Deficit<br>Hyperactivity Disorder</li>
      <li>Autism Spectrum Disorder</li>
      <li>Specific Learning Disorders</li>
      <li>Language disorders</li>
      <li>Anxiety Disorders</li>
      <li>Mood Disorders</li>
      <li>Communication Disorders</li>
    </ul>
    <div class="body-copy" style="position:absolute;top:567px;left:38px;right:38px">
      <p>We are passionate about collaborating with your school or workplace, supporting you in applying for financial support if available (such as NDIS funding), and to feel more informed and confident in your decisions.</p>
    </div>
    <div class="footer-bar footer-soft">www.<b>brightpathclinic</b>.com.au</div>
  </div>

  <!-- process -->
  <div class="panel panel-white">
    <div style="position:absolute;top:30px;width:100%"><span class="tag tag-blue">THE PROCESS</span></div>
    <div class="process">
      <div class="proc-step" style="top:40px"><div class="proc-box">An initial face-to-face interview to discuss your concerns and understand the relevant history and details.</div><div class="proc-num">1</div></div>
      <div class="proc-step" style="top:157px"><div class="proc-box">A formal assessment sessions during which relevant tests are completed. This can include IQ testing, Achievement testing, Memory testing, Personality profiling etc.</div><div class="proc-num">2</div></div>
      <div class="proc-step" style="top:274px"><div class="proc-box">obtaining additional information through questionnaires, observation, contact with other professionals (such as teachers/tutors etc).</div><div class="proc-num">3</div></div>
      <div class="proc-step" style="top:391px"><div class="proc-box">A feedback session during which we provide you with a final draft of the report and discuss possible recommendations, collaborating about the next steps.</div><div class="proc-num">4</div></div>
      <div class="proc-step" style="top:508px"><div class="proc-box">A copy of the finalised report is provided and opportunity for discussion and engagement with teachers or other allied health is provided.</div><div class="proc-num">5</div></div>
    </div>
    <div class="footer-bar footer-green">hello@brightpathclinic.com.au</div>
  </div>
</section>

</body>
</html>
```